We are a video game localization/translation company. In other words, we localize/translate video games into other languages. Our target customers are video game developers and publishers who make and publish games on all platforms (consoles, PC, mobile, web). The design should be in line with this description and should subtly relate to video games (without being too playful, we want to preserve some seriousness). You can have a look at our website to get some ideas, but you do not have to follow the same style: [login to view URL]

The stationery is to include:
- Business card (size: 3.50x2.00 inches excluding the bleed)
- Letterhead (size: 8.5x11 inches excluding the bleed)
- Presentation Folder (9x12 inches with Left & Right 4" Pockets)
- Envelope (size: 4.125 x 9.5 inches, excluding the bleed; no window)

Specifications:
Bleed & Trim
1/8" on all sides of the document will be trimmed off, this is called the bleed. So the size of the file that you submit needs to be 1/4" higher and wider than the finished (cut) size. Make sure that all background images and colors extend into this area to avoid having a white frame around your design.
Safe Zone
Additionally, please adjust your text and important graphics to be 1/8" inside of the finished size on all four sides.
Colors
The file needs to be in CYMK color not RGB
Resolution
The resolution of your file needs to be 300dpi
Submitting Files
We prefer a pdf file (1 file for each side), if this is not possible please send a psd, ai or eps file. Make sure all fonts are converted to outline. After making your order you will be prompted to upload your print-ready files.
Blacks
Rich black ( 40% Cyan, 40% Magenta, 30% Yellow, 100% Black ) should be used for large areas of black and will give a deep solid black finish.
100% black ( 0% Cyan, 0% Magenta, 0% Yellow, 100% Black ) should be used for small black text (12pt and smaller) and lines, this will result in crisp text and edges.

Please find attached our logo. You may play with the logo as well, for example, you can use only "Velorin" or only the text part or only the logo.

Information to be used on the business card:
Dario Lutfi Orbeson
Game localization expert
4178 Quillmere Crescent, Ottawa, ON, Canada K2P 7R3
613-482-6954
dario@velorinloc.example
[login to view URL]
Slogan: Let's take you to new markets

P.S. A QR code may be nice.

Information to be used on the letterhead and the envelope:
Velorin Translation Services Ltd.
613-482-6954
contactus@velorinloc.example
[login to view URL]

```html
<!DOCTYPE html>
<html lang="en">
<head>
<meta charset="utf-8">
<title>Velorin Stationery</title>
<link rel="stylesheet" href="https://fonts.googleapis.com/css2?family=Lato:wght@400;700&family=Montserrat:wght@500&display=swap">
<style>
:root{
  --backdrop:#dcd8df;
  --paper:#f7f8f8;
  --teal-dark:#176d6e;
  --teal-light:#3fbfc0;
  --ink:#3b3b3b;
  --ink-soft:#6e6e6e;
}
*{box-sizing:border-box;margin:0;padding:0}
html,body{width:1200px;height:900px;overflow:hidden}
body{background:var(--backdrop);font-family:'Lato',sans-serif;color:var(--ink);position:relative}
.sheet{position:absolute;background:var(--paper);box-shadow:0 2px 6px rgba(0,0,0,.12);overflow:hidden}
.wave{position:absolute;left:0;bottom:0;width:100%;display:block}
.brand{display:flex;align-items:center;gap:8px;font-family:'Montserrat',sans-serif;font-weight:500;color:var(--teal-dark);letter-spacing:.04em;position:absolute}
.brand-dot{border:2px solid var(--teal-light);border-radius:50%}
.contact{list-style:none;font-size:10px;color:var(--ink-soft);line-height:1.55}
.contact .icon{display:inline-block;width:8px;height:8px;margin-right:5px;vertical-align:-1px}
.contact svg{width:8px;height:8px;fill:var(--teal-light)}

/* Letterhead */
.letterhead{left:47px;top:93px;width:509px;height:716px}
.letterhead .brand{left:37px;top:45px;font-size:21px}
.letterhead .brand-dot{width:30px;height:30px}
.letterhead .divider{position:absolute;left:324px;top:29px;width:1px;height:74px;background:var(--teal-dark)}
.letterhead .contact{position:absolute;left:347px;top:30px}
.letter{position:absolute;left:37px;top:186px;width:440px;font-size:9.2px;line-height:1.45;color:var(--ink)}
.letter p{margin-bottom:12px}
.letter .recipient{margin-bottom:14px}
.letter .salutation{font-size:11px;font-weight:700;margin-bottom:18px}
.letter .closing{margin-top:22px}
.signature{display:block;width:58px;height:14px;background:linear-gradient(90deg,#c9c9c9,#9a9a9a);opacity:.5;margin:6px 0 4px;border-radius:3px}

/* Envelope back */
.envelope-back{left:576px;top:64px;width:571px;height:280px}
.flap{position:absolute;left:0;top:0;width:100%;height:108px}
.flap-mark{position:absolute;left:264px;top:28px;width:40px;height:40px;border:2px solid var(--teal-light);border-radius:50%}

/* Envelope front */
.envelope-front{left:576px;top:357px;width:571px;height:279px}
.envelope-front .brand{left:37px;top:42px;font-size:21px}
.envelope-front .brand-dot{width:30px;height:30px}
.envelope-front .contact{position:absolute;left:37px;top:152px}

/* Business cards */
.card{top:652px;width:269px;height:157px;border-radius:12px}
.card-front{left:576px}
.card-front .brand{left:26px;top:64px;font-size:15px;gap:6px}
.card-front .brand-dot{width:22px;height:22px}
.card-front .divider{position:absolute;left:139px;top:38px;width:1px;height:70px;background:var(--teal-dark)}
.card-front .person{position:absolute;left:152px;top:38px}
.person-name{font-size:10px;font-weight:700;color:var(--teal-dark)}
.person-role{font-size:7px;color:var(--ink-soft);margin-bottom:9px}
.card-front .contact{font-size:6.4px;line-height:1.6}
.card-front .contact .icon,.card-front .contact svg{width:6px;height:6px}
.card-back{left:877px;background:var(--teal-dark)}
.card-back .brand{left:58px;top:58px;font-size:22px;color:#fff;gap:8px}
.card-back .brand-dot{width:28px;height:28px;border-color:#fff}
.slogan{position:absolute;left:0;width:100%;top:128px;text-align:center;font-size:7px;color:#cfe9e9;letter-spacing:.03em}
</style>
</head>
<body>

<section class="sheet letterhead">
  <div class="brand"><span class="brand-dot"></span>VELORIN</div>
  <div class="divider"></div>
  <ul class="contact">
    <li>4178 Quillmere Crescent, Ottawa</li>
    <li>ON, Canada K2P 7R3</li>
    <li><span class="icon"><svg viewBox="0 0 10 10"><path d="M2 0h2l1 3-1.5 1a6 6 0 0 0 2.5 2.5L7 5l3 1v2a2 2 0 0 1-2 2A8 8 0 0 1 0 2a2 2 0 0 1 2-2z"/></svg></span>613-482-6954</li>
    <li><span class="icon"><svg viewBox="0 0 10 10"><path d="M0 2h10v6H0z"/></svg></span>dario@velorinloc.example</li>
    <li><span class="icon"><svg viewBox="0 0 10 10"><circle cx="5" cy="5" r="5"/></svg></span>www.velorinloc.example</li>
  </ul>
  <div class="letter">
    <p>September 19, 2018</p>
    <p class="recipient">Mr. Alden Prewitt<br>President<br>Brightwell Holdings Group<br>111 Street Name, Suite# 01<br>City, State, 123450</p>
    <p><strong>Subject :</strong> <strong>Lorem ipsum dolor sit amet, consectetur adipiscing elit, sed do eiusmod tempor.</strong></p>
    <p class="salutation">Dear Mr. Corwin Tally</p>
    <p>Lorem ipsum dolor sit amet, consectetur adipiscing elit, sed do eiusmod tempor incididunt ut labore et dolore magna aliqua. Ut enim ad minim veniam, quis nostrud exercitation ullamco laboris nisi ut aliquip ex ea commodo consequat. Duis aute irure dolor.</p>
    <p>Lorem ipsum dolor sit amet, consectetur adipiscing elit, sed do eiusmod tempor incididunt ut labore et dolore magna aliqua. Ut enim ad minim veniam, quis nostrud exercitation ullamco laboris nisi ut aliquip ex ea commodo consequat. Duis aute irure dolor. in reprehenderit in voluptate velit esse cillum dolore eu fugiat nulla tat non proident, sunt in culpa qui officia deserunt mollit anim id est laborum.</p>
    <p>Lorem ipsum dolor sit amet, consectetur adipiscing elit, sed do eiusmod tempor incididunt ut labore et dolore magna aliqua. Ut enim ad minim veniam, quis nostrud exercitation ullamco laboris nisi ut aliquip ex ea commodo consequat. Duis aute irure dolor. in reprehenderit in voluptate velit esse cillum dolore eu fugiat nulla tat non proident, sunt in culpa qui officia deserunt mollit anim id est laborum.Lorem ipsum dolor sit amet, consectetur adipiscing elit, sed do eiusmod tempor incididunt.</p>
    <p>Lorem ipsum dolor sit amet, consectetur adipiscing elit, sed do eiusmod tempor incididunt ut labore et dolore magna aliqua. Ut enim ad minim veniam, quis nostrud exercitation ullamco.</p>
    <p class="closing">Sincerely Yours<span class="signature" role="img" aria-label="Handwritten signature"></span>Corwin Tally<br>Managing Director</p>
  </div>
  <svg class="wave" viewBox="0 0 509 62" height="62" preserveAspectRatio="none">
    <path d="M0 26 C150 8 330 10 509 0" fill="none" stroke="var(--teal-light)" stroke-width="4"/>
    <path d="M0 30 C170 22 340 18 509 6 L509 62 L0 62Z" fill="var(--teal-dark)"/>
  </svg>
</section>

<section class="sheet envelope-back">
  <svg class="flap" viewBox="0 0 571 108" preserveAspectRatio="none">
    <path d="M0 0H571V20L551 80Q544 106 518 106H53Q27 106 20 80L0 20Z" fill="var(--teal-dark)"/>
  </svg>
  <span class="flap-mark"></span>
</section>

<section class="sheet envelope-front">
  <div class="brand"><span class="brand-dot"></span>VELORIN</div>
  <ul class="contact">
    <li>4178 Quillmere Crescent, Ottawa</li>
    <li>ON, Canada K2P 7R3</li>
    <li><span class="icon"><svg viewBox="0 0 10 10"><path d="M2 0h2l1 3-1.5 1a6 6 0 0 0 2.5 2.5L7 5l3 1v2a2 2 0 0 1-2 2A8 8 0 0 1 0 2a2 2 0 0 1 2-2z"/></svg></span>613-482-6954</li>
    <li><span class="icon"><svg viewBox="0 0 10 10"><path d="M0 2h10v6H0z"/></svg></span>dario@velorinloc.example</li>
    <li><span class="icon"><svg viewBox="0 0 10 10"><circle cx="5" cy="5" r="5"/></svg></span>www.velorinloc.example</li>
  </ul>
  <svg class="wave" viewBox="0 0 571 62" height="62" preserveAspectRatio="none">
    <path d="M0 28 C180 26 380 18 571 0" fill="none" stroke="var(--teal-light)" stroke-width="4"/>
    <path d="M0 34 C200 32 400 24 571 8 L571 62 L0 62Z" fill="var(--teal-dark)"/>
  </svg>
</section>

<section class="sheet card card-front">
  <div class="brand"><span class="brand-dot"></span>VELORIN</div>
  <div class="divider"></div>
  <div class="person">
    <div class="person-name">Dario Lutfi Orbeson</div>
    <div class="person-role">Game localization expert</div>
    <ul class="contact">
      <li>4178 Quillmere Crescent, Ottawa</li>
      <li>ON, Canada K2P 7R3</li>
      <li><span class="icon"><svg viewBox="0 0 10 10"><path d="M2 0h2l1 3-1.5 1a6 6 0 0 0 2.5 2.5L7 5l3 1v2a2 2 0 0 1-2 2A8 8 0 0 1 0 2a2 2 0 0 1 2-2z"/></svg></span>613-482-6954</li>
      <li><span class="icon"><svg viewBox="0 0 10 10"><path d="M0 2h10v6H0z"/></svg></span>dario@velorinloc.example</li>
      <li><span class="icon"><svg viewBox="0 0 10 10"><circle cx="5" cy="5" r="5"/></svg></span>www.velorinloc.example</li>
    </ul>
  </div>
  <svg class="wave" viewBox="0 0 269 24" height="24" preserveAspectRatio="none">
    <path d="M0 10 C90 10 180 6 269 0" fill="none" stroke="var(--teal-light)" stroke-width="3"/>
    <path d="M0 14 C90 13 180 10 269 3 L269 24 L0 24Z" fill="var(--teal-dark)"/>
  </svg>
</section>

<section class="sheet card card-back">
  <div class="brand"><span class="brand-dot"></span>VELORIN</div>
  <p class="slogan">Let's take you to new markets</p>
</section>

</body>
</html>
```